Backup Software Tri-fold Brochure Project

We need a great looking and informative brochure to describe our new Backup Software offering. The brochures are to be used in retail and small business environments given to clients interested in protecting their computer from data loss.
The brochure should include attractive imagery that conveys a sense of Trust and Security to the prospective client.
The copy is provided as an attachment to this project. We'd like our Bright Deskpoint product logo to be printed on the back cover. The logo is attached to this project.
The finished tri-fold brochure will be submitted to Plumcopy for printing as an 8.5" x 11" tri-fold brochure. Their design instructions are online http://plumcopy-example.com/custom-brochures.aspx.
The finished product should be Adobe Illustrator CS3 (*.ai) with a PDF Proof.
Target Market(s)
Retail and Small Business customers
Industry/Entity Type
Software
Designer to choose colors to be used in the design.

```html
<!DOCTYPE html>
<html lang="en">
<head>
<meta charset="utf-8">
<title>Bright Deskpoint – Tri-fold Brochure</title>
<link rel="stylesheet" href="https://fonts.googleapis.com/css2?family=Anton&family=Lato:wght@400;700&family=Roboto:wght@500;700&display=swap">
<style>
  :root{
    --green:#4cbb1f;
    --green-light:#6fd22f;
    --green-dark:#2f9a14;
    --blue:#1a5ba6;
    --blue-dark:#0f3f82;
    --navy:#0b1f45;
    --white:#ffffff;
    --ink:#111111;
    --page:#e6e9ec;
  }
  *{margin:0;padding:0;box-sizing:border-box}
  html,body{width:1200px;height:1200px;overflow:hidden;background:var(--page)}
  .brochure{position:absolute;left:0;top:130px;width:1200px;height:940px;overflow:hidden;background:var(--white)}
  .brochure-art{position:absolute;inset:0}
  .txt{position:absolute;font-family:"Roboto",Arial,sans-serif}
  .panel-title{left:0;width:400px;top:478px;text-align:center;font-size:29px;font-weight:700;color:var(--blue)}
  .body-copy{left:22px;width:352px;font-family:"Lato",Arial,sans-serif;font-size:12.6px;line-height:15.6px;color:var(--ink);text-align:justify}
  .copy-1{top:527px}
  .copy-2{top:652px}
  .copy-3{top:730px}
  .site-url{font-family:"Lato",Arial,sans-serif;font-size:16px;font-weight:700;letter-spacing:3px;color:var(--white);text-align:center;width:400px;top:902px}
  .url-left{left:0}
  .url-right{left:800px}
  .middle-lead{left:440px;width:320px;top:135px;text-align:center;color:var(--white);font-size:19.5px;font-weight:500;line-height:24px}
  .or-badge{left:545px;top:228px;width:120px;height:120px;text-align:center;line-height:118px;font-size:50px;font-weight:700;color:var(--white)}
  .middle-offer{left:444px;width:306px;top:380px;color:var(--white);font-size:20.5px;font-weight:500;line-height:24px;letter-spacing:.3px;text-align:justify;text-align-last:center}
  .brand-name{font-weight:700;color:var(--blue);letter-spacing:.5px}
  .brand-mid{left:400px;width:400px;top:800px;text-align:center;font-size:22px}
  .brand-right{left:800px;width:400px;top:52px;text-align:center;font-size:30px}
  .call-line{left:400px;width:400px;top:874px;text-align:center;font-size:25px;font-weight:700;color:var(--green)}
  .headline{left:800px;width:400px;text-align:center}
  .headline-small{top:686px;font-size:37px;font-weight:700;color:var(--blue)}
  .headline-big{top:728px;font-family:"Anton","Impact",sans-serif;font-size:58px;color:var(--green);letter-spacing:1px}
</style>
</head>
<body>
<div class="brochure">
  <svg class="brochure-art" width="1200" height="940" viewBox="0 0 1200 940" xmlns="http://www.w3.org/2000/svg">
    <defs>
      <linearGradient id="techPhoto" x1="0" y1="0" x2="1" y2="1">
        <stop offset="0" stop-color="#0a1a3c"/>
        <stop offset=".45" stop-color="#2a67b8"/>
        <stop offset="1" stop-color="#0b1f45"/>
      </linearGradient>
      <linearGradient id="greenField" x1="0" y1="0" x2="0" y2="1">
        <stop offset="0" stop-color="#5ccc24"/>
        <stop offset="1" stop-color="#3fb01a"/>
      </linearGradient>
      <linearGradient id="greyCollage" x1="0" y1="0" x2="0" y2="1">
        <stop offset="0" stop-color="#f4f5f6"/>
        <stop offset="1" stop-color="#d9dcdf"/>
      </linearGradient>
      <radialGradient id="globePhoto" cx=".35" cy=".5" r=".7">
        <stop offset="0" stop-color="#3f86d8"/>
        <stop offset=".5" stop-color="#b9c9db"/>
        <stop offset="1" stop-color="#f3f5f7"/>
      </radialGradient>
    </defs>

    <!-- Left panel -->
    <rect x="0" y="0" width="400" height="940" fill="url(#greenField)"/>
    <rect x="0" y="0" width="400" height="470" fill="url(#techPhoto)" role="img" aria-label="Photo of a hand holding a glowing tablet with a globe, laptop and network icons"/>
    <path d="M0,418 C110,370 260,380 400,470 L400,940 L0,940 Z" fill="var(--green)"/>
    <path d="M0,445 C110,398 260,408 400,500 L400,862 C280,885 130,855 0,800 Z" fill="var(--white)"/>
    <path d="M0,812 C130,866 280,896 400,874" fill="none" stroke="var(--blue)" stroke-width="9"/>

    <!-- Middle panel -->
    <rect x="400" y="0" width="400" height="940" fill="url(#greyCollage)"/>
    <rect x="400" y="700" width="400" height="240" fill="url(#greyCollage)" opacity=".9" role="img" aria-label="Faint collage of a globe and computer screens"/>
    <path d="M400,0 H800 V668 C700,700 600,660 520,596 C470,556 430,528 400,512 Z" fill="url(#greenField)"/>
    <path d="M400,532 C432,550 472,582 522,624 C604,692 704,716 800,688" fill="none" stroke="var(--blue)" stroke-width="13"/>
    <circle cx="605" cy="288" r="60" fill="var(--blue)" stroke="var(--white)" stroke-width="4"/>
    <rect x="484" y="806" width="20" height="20" fill="var(--green)"/>

    <!-- Right panel -->
    <rect x="800" y="0" width="400" height="940" fill="var(--white)"/>
    <rect x="800" y="140" width="400" height="300" fill="url(#globePhoto)" role="img" aria-label="Photo of hands touching a glowing globe and floating screens"/>
    <path d="M800,640 C900,520 1080,480 1200,300 L1200,400 C1100,540 930,580 820,660 Z" fill="var(--blue)"/>
    <path d="M806,672 C910,580 1080,560 1200,420 L1200,600 C1080,560 920,600 812,682 Z" fill="var(--green)"/>
    <path d="M800,690 C880,600 1040,540 1200,620 L1200,790 C1080,860 900,860 800,850 Z" fill="var(--white)"/>
    <path d="M1040,566 C1110,578 1160,600 1200,626" fill="none" stroke="var(--blue)" stroke-width="10"/>
    <path d="M800,852 C900,872 1080,862 1200,782 L1200,940 L800,940 Z" fill="var(--blue)"/>
    <path d="M800,846 C900,866 1080,856 1200,776" fill="none" stroke="var(--green)" stroke-width="8"/>
    <rect x="852" y="58" width="26" height="26" fill="var(--green)"/>
  </svg>

  <h2 class="txt panel-title">How It Works</h2>
  <p class="txt body-copy copy-1">Our technology is designed to take advantage of the powerful imaging technology Embedded in corvane fenestra. Deep within the core of the os is an imaging Engine that can create a point-in-time backup of the fenestra operating system, device drivers, programs and system state. The backup can be used later to Recover the system back to this point-in-time.</p>
  <p class="txt body-copy copy-2">Backups created by our imaging technology can even be used to restore Fenestra to dissimilar hardware. This is a quick way to migrate to a new computer Without having to reinstall everything from scratch.</p>
  <p class="txt body-copy copy-3">Our technology stores backups as corvane "Virtual hard disk" (vhd). These Vhd files can be directly mounted from the fenestra disk manager. This is a Great way to browse the contents of your image backup and restore individual Files and folders.</p>
  <p class="txt site-url url-left">www.yourwebsite.com</p>

  <p class="txt middle-lead">Call us to schedule a day to bring in your computer.</p>
  <p class="txt or-badge">OR</p>
  <p class="txt middle-offer">Once a month we do "Image Backup Saturday". Drop off your computer in the morning and pick it up a few hours later. Call for a copy of our schedule.</p>
  <p class="txt brand-name brand-mid">Bright Deskpoint</p>
  <p class="txt call-line">CALL US ON-000 0000 000</p>

  <p class="txt brand-name brand-right">&nbsp;&nbsp;Bright Deskpoint</p>
  <p class="txt headline headline-small">The best backup for</p>
  <p class="txt headline headline-big">YOUR CLIENTS</p>
  <p class="txt site-url url-right">www.yourwebsite.com</p>
</div>
</body>
</html>
```